Lira Vantell Music Flyer for Social Media

The flyer needs to include the networks Lira Vantell music is distributed on such as TuneHarbor, WaveCastFM, Brook, and Soundly. This flyer will be posted on social media websites such as friendloop, Pictogrove, and Chirpnet. The flyer will also be listed on the music artist official website. The artist logo is attached for additional creative ideas.

Target Market(s)

Music lovers

Industry/Entity Type

Music Download

Requirements
Must have
• Must have the music networks listed on the photo and the artist name.
Nice to have
• It would be nice to have the website listed: www.liravantell.example and artist logo.
Should not have
• Anything that is not listed in the project description.

```html
<!DOCTYPE html>
<html lang="en">
<head>
<meta charset="utf-8">
<title>Lira Vantell Music Flyer</title>
<link href="https://fonts.googleapis.com/css2?family=Arimo:wght@400;700&display=swap" rel="stylesheet">
<style>
  :root {
    --page-bg: #2a1d17;
    --flyer-brown: #5a3418;
    --flyer-amber: #c27a2c;
    --flyer-plum: #5e3a5c;
    --flyer-dark: #24140e;
    --hair-dark: #241418;
    --skin-warm: #b56a4e;
    --skin-light: #e0a07e;
    --sweater-light: #e8e4e6;
    --band-bg: rgba(45, 32, 28, 0.78);
    --text-light: #ffffff;
    --badge-dark: #000000;
    --badge-light: #ffffff;
    --text-dark: #222222;
  }
  * { margin: 0; padding: 0; box-sizing: border-box; }
  html, body { width: 1200px; height: 1200px; overflow: hidden; }
  body {
    background: var(--page-bg);
    font-family: "Arimo", Arial, sans-serif;
    position: relative;
  }
  .flyer {
    position: absolute;
    left: 200px;
    top: 30px;
    width: 800px;
    height: 1140px;
    overflow: hidden;
    background: var(--flyer-dark);
  }
  .flyer-photo {
    position: absolute;
    inset: 0;
    background:
      radial-gradient(ellipse 22% 26% at 70% 44%, var(--skin-light) 0%, var(--skin-warm) 55%, transparent 100%),
      radial-gradient(ellipse 32% 36% at 71% 42%, rgba(160, 90, 70, 0.95) 0%, rgba(160, 90, 70, 0.6) 55%, transparent 80%),
      radial-gradient(ellipse 38% 30% at 92% 98%, var(--sweater-light) 0%, rgba(220, 214, 220, 0.7) 45%, transparent 75%),
      radial-gradient(ellipse 50% 55% at 74% 42%, var(--hair-dark) 0%, rgba(36, 20, 24, 0.9) 60%, transparent 85%),
      radial-gradient(ellipse 45% 40% at 22% 58%, var(--flyer-amber) 0%, rgba(194, 122, 44, 0.5) 45%, transparent 75%),
      linear-gradient(165deg, var(--flyer-brown) 0%, #7a4a2a 35%, var(--flyer-plum) 70%, var(--flyer-dark) 100%);
  }
  .flyer-shade {
    position: absolute;
    inset: 0;
    background: linear-gradient(180deg, transparent 70%, rgba(30, 18, 12, 0.55) 100%);
  }
  .artist-mark {
    position: absolute;
    left: 43px;
    top: 790px;
    display: flex;
    align-items: center;
    gap: 12px;
    color: var(--text-light);
    font-weight: 400;
    font-size: 20px;
    letter-spacing: 13px;
    text-transform: uppercase;
  }
  .artist-mark .mark-dot {
    width: 10px; height: 10px; border-radius: 50%;
    background: var(--text-light);
  }
  .name-band {
    position: absolute;
    left: 0;
    top: 841px;
    width: 560px;
    height: 71px;
    background: linear-gradient(90deg, var(--band-bg) 65%, rgba(45, 32, 28, 0));
    display: flex;
    align-items: center;
    padding-left: 43px;
  }
  .name-band h1 {
    color: var(--text-light);
    font-weight: 700;
    font-size: 48px;
    white-space: nowrap;
  }
  .networks {
    position: absolute;
    left: 39px;
    top: 997px;
    display: flex;
    gap: 26px;
    list-style: none;
  }
  .network {
    width: 161px;
    height: 76px;
    display: flex;
    align-items: center;
    justify-content: center;
    font-weight: 700;
    font-size: 22px;
  }
  .network--dark { background: var(--badge-dark); color: var(--badge-light); }
  .network--light { background: var(--badge-light); color: var(--text-dark); }
  .website {
    position: absolute;
    left: 0; right: 0;
    top: 1084px;
    text-align: center;
    color: var(--text-light);
    font-size: 28px;
    font-weight: 400;
  }
</style>
</head>
<body>
  <main class="flyer">
    <div class="flyer-photo" role="img" aria-label="Portrait photo of the smiling artist with curly dark hair and a striped sweater, over a warm amber background with faint music notes and a treble clef"></div>
    <div class="flyer-shade"></div>

    <div class="artist-mark"><span class="mark-dot"></span>Lira Vantell</div>

    <div class="name-band"><h1>LIRA VANTELL, LLC</h1></div>

    <ul class="networks">
      <li class="network network--dark">Brook</li>
      <li class="network network--light">WaveCastFM</li>
      <li class="network network--light">Soundly</li>
      <li class="network network--dark">TuneHarbor</li>
    </ul>

    <p class="website">www.liravantell.example</p>
  </main>
</body>
</html>
```